"Recently Leased" flyer for real estate agency

Looking to have a Recently Leased flyer designed. This will be delivered to apartments and houses closely situated to a property we have recently leased. The idea is to get the attention of owner/landlords in the area that may be considering leasing their property in the future and inform them of the great work we are doing locally. I would like the design to be a two sided flyer using the photoshop (PSD) template below (we would like to be able to edit this once complete should we need to update copy etc in the future). I would like the front page to look like our "for lease sign with the leased sticker on it and copy, I dont want it to look like a typical junk mail flyer.

Target Market(s)

Property owners and investors, male and female aged 28-70

Industry/Entity Type

Real Estate

Font styles to use
Sans Serif

Colors

Designer to choose colors to be used in the design.

Requirements
Must have
• Harbor Keystone Logo
• Contact information
• Copy supplied
Nice to have
• Slick, clean design,
Should not have
• too many colours or too busy a design.
• NO PROPERTY PHOTOS ON FRONT - I want this to be generic and not relate to a specific property image which might confuse people.

```html
<!DOCTYPE html>
<html lang="en">
<head>
<meta charset="utf-8">
<title>Harbor Keystone – Recently Leased Flyer</title>
<link href="https://fonts.googleapis.com/css2?family=Lato:ital,wght@0,400;0,700;0,900;1,400;1,700&display=swap" rel="stylesheet">
<style>
  :root{
    --backdrop:#e8e4de;
    --slate-dark:#27353c;
    --slate-mid:#3d4f57;
    --teal:#1fa9ae;
    --teal-text:#14879a;
    --band:#0d5d76;
    --ink:#1f2326;
    --paper:#ffffff;
    --tag:#111111;
  }
  *{box-sizing:border-box;margin:0;padding:0}
  html,body{width:1200px;height:750px;overflow:hidden}
  body{background:var(--backdrop);font-family:'Lato',sans-serif;position:relative}

  .flyer{position:absolute;top:25px;width:340px;height:700px;background:var(--paper);overflow:hidden;box-shadow:0 6px 18px rgba(0,0,0,.18)}
  .flyer--intro{left:230px}
  .flyer--leased{left:630px}

  .hero{position:absolute;inset:0 0 auto 0;height:270px;
    background:linear-gradient(160deg,var(--slate-mid) 0%,var(--slate-dark) 60%,#2d4a3c 100%)}
  .brand{position:absolute;top:38px;left:0;right:0;text-align:center;color:var(--paper);
    font-weight:900;font-size:27px;letter-spacing:1px;text-transform:uppercase}
  .brand-mark{display:inline-block;width:9px;height:9px;background:var(--teal);margin-right:8px;vertical-align:middle}
  .hero-copy{position:absolute;top:100px;left:30px;right:30px;text-align:center;color:var(--paper);font-size:12.5px;line-height:1.35}
  .hero-copy p+p{margin-top:8px}

  .accent{position:absolute;top:222px;left:0;right:0;bottom:0;background:var(--teal);
    clip-path:polygon(0 28px,100% 0,100% 100%,0 100%)}
  .sheet{position:absolute;top:228px;left:0;right:0;bottom:0;background:var(--paper);
    clip-path:polygon(0 28px,100% 0,100% 100%,0 100%)}

  .body-copy{position:absolute;top:264px;left:28px;right:24px;bottom:116px;display:flex;flex-direction:column;gap:14px}

  .points{list-style:none;color:var(--ink);font-size:11px;line-height:1.28;font-weight:700}
  .points li{position:relative;padding-left:18px;margin-bottom:5px}
  .points li:last-child{margin-bottom:0}
  .points--dots li::before{content:"";position:absolute;left:3px;top:5px;width:5px;height:5px;border-radius:50%;background:var(--ink)}
  .points--ticks li{margin-bottom:8px}
  .points--ticks svg{position:absolute;left:0;top:1px;width:12px;height:12px}

  .call{color:var(--teal-text);font-size:11px;line-height:1.35;font-style:italic;padding-right:4px}
  .flyer--intro .call{text-align:center}
  .flyer--leased .call{text-align:left}

  .band{position:absolute;left:0;right:0;bottom:0;height:112px;background:var(--band);
    clip-path:polygon(0 26px,100% 0,100% 100%,0 100%)}
  .name-tag{position:absolute;bottom:72px;left:50%;transform:translateX(-50%);background:var(--tag);color:var(--paper);
    padding:6px 16px 5px;text-align:center;min-width:190px}
  .name-tag strong{display:block;font-weight:900;font-size:21px;letter-spacing:1px;text-transform:uppercase;line-height:1}
  .name-tag span{display:block;font-size:8px;letter-spacing:1.5px;text-transform:uppercase;margin-top:2px}
  .contact{position:absolute;left:0;right:0;bottom:12px;text-align:center;color:var(--paper);font-size:11px;line-height:1.45;font-weight:700}
</style>
</head>
<body>

<article class="flyer flyer--intro">
  <div class="hero" role="img" aria-label="Dimmed photograph of a modern residential street frontage"></div>
  <div class="brand"><span class="brand-mark"></span>Harbor Keystone</div>
  <div class="hero-copy">
    <p>The fundamental idea behind Harbor Keystone Agency was to give landlords a simple and confidence inspiring experience. We achieve this through:</p>
  </div>
  <div class="accent"></div>
  <div class="sheet"></div>
  <div class="body-copy">
    <ul class="points points--dots">
      <li>Unique marketing that goes beyond the standard listing sites and has seen our average days-on-market at 5.9days for 2018.</li>
      <li>A simple, yet competitive fee structure.</li>
      <li>Excellent customer service through an experienced professional property manager.</li>
      <li>Sound advice and communication throughout the leasing and management process.</li>
      <li>A simple yet powerful landlord portal that enables owners to view media rich inspection reports, financial reports and maintenance at anytime.</li>
      <li>We then back our service promise with a money back guarantee.</li>
    </ul>
    <p class="call">If you have been considering leasing or purchasing a local investment or are unhappy with your current managing agency, please contact your local rental specialist.</p>
  </div>
  <div class="band"></div>
  <div class="name-tag"><strong>Sam Carver</strong><span>Harbor Keystone Agency</span></div>
  <div class="contact">
    Level 2, 18 Seaview Rd, Harbourside NSW 2100<br>
    www.harborkeystoneagency.com.au<br>
    0400 555 218 | sam@harborkeystoneagency.com.au
  </div>
</article>

<article class="flyer flyer--leased">
  <div class="hero" role="img" aria-label="Dimmed photograph of apartment buildings along a leafy street"></div>
  <div class="brand"><span class="brand-mark"></span>Harbor Keystone</div>
  <div class="hero-copy">
    <p>We recently leased a property in your building or street. Attracting a great reliable tenant and fantastic return for the owner.</p>
    <p>We received a high number of enquires and applications for this property and have a database of screened and qualified tenants looking to lease in your area.</p>
  </div>
  <div class="accent"></div>
  <div class="sheet"></div>
  <div class="body-copy">
    <ul class="points points--ticks">
      <li><svg viewBox="0 0 12 12"><path d="M1.5 6.5l3 3 6-7" fill="none" stroke="#1fa9ae" stroke-width="2"/></svg>On average we lease properties 2 weeks faster than the Coastal District average</li>
      <li><svg viewBox="0 0 12 12"><path d="M1.5 6.5l3 3 6-7" fill="none" stroke="#1fa9ae" stroke-width="2"/></svg>Strong database of tenants actively looking in the area</li>
      <li><svg viewBox="0 0 12 12"><path d="M1.5 6.5l3 3 6-7" fill="none" stroke="#1fa9ae" stroke-width="2"/></svg>All we do is lease property, no sales – so tenanting and managing your property is our priority</li>
      <li><svg viewBox="0 0 12 12"><path d="M1.5 6.5l3 3 6-7" fill="none" stroke="#1fa9ae" stroke-width="2"/></svg>90 day money back guarantee on our level of service</li>
      <li><svg viewBox="0 0 12 12"><path d="M1.5 6.5l3 3 6-7" fill="none" stroke="#1fa9ae" stroke-width="2"/></svg>Highly competitive, simple all-inclusive pricing.</li>
      <li><svg viewBox="0 0 12 12"><path d="M1.5 6.5l3 3 6-7" fill="none" stroke="#1fa9ae" stroke-width="2"/></svg>Experience the difference of a property management specialist</li>
    </ul>
    <p class="call">Contact Sam to get your free rental appraisal or transfer your existing investment to an agency that will give it the attention it deserves and maximise your return.</p>
  </div>
  <div class="band"></div>
  <div class="name-tag"><strong>Sam Carver</strong><span>Harbor Keystone Agency</span></div>
  <div class="contact">
    Level 2, 18 Seaview Rd, Harbourside NSW 2100<br>
    www.harborkeystoneagency.com.au<br>
    0400 555 218 | sam@harborkeystoneagency.com.au
  </div>
</article>

</body>
</html>
```